Business Card & Logo Design - Hedge Fund

We need a business card and logo design for a hedge fund. The hedge fund is named Morvane Equity LLC. Morvane Equity was created by finance professors and the strategy is based academic research that looks for patterns in stock prices. The design should look conservative, solid, strong. We favor a classic style - nothing flashy. The logo can relate to the name Morvane Equity, or it could involve a symbol design that connotes "science" . We are open to ideas. We do not want alot of colors - but if any, color - blue is preferred. The font that seems to look best for the name (Morvane Equity) is arial black. We are open to ideas. Most important - we want to see a mock up of an actual business card with the logo concept embedded. The business card should include space for : company name, individual name, position title, cell phone, address. We hope to have this work done by Sept. 8.

Target Market(s)

We will be meeting with and giving the business card to institutions and high net worth individuals.

Industry/Entity Type

Investment Advisory

Contact Information for Business Card

Company name - Morvane Equity LLC
Individual name - Peter Dalby
Title - Portfolio Manager
Cell - (412) 555-0187
Address - 2650 Birchmont Lane, Suite 300, Atlanta GA 30327

Font styles to use
Other font styles liked:
• Arial

Colors
3277b5
0255a3
85acd3
cedeed
fdf9cf
d9d9d9
e6e6e6
f04a50
6b449b

Requirements
Must have
• Must have card details that are sited above.
• We would like a logo related to the name (Morvane Equity) or concept of the fund.
Nice to have
• We want conservative / understated / clean crisp look.
• If any colors - we prefer conservative appearance - blue / gray.
• I have enclosed an example of a card style that looks attractive - please do not exactly copy this card. This is not our company or logo. I feel the layout is attractive - just as an example
Should not have
• Avoid too much color.
• I have selected some preferred colors. Please do not use all of the colors - I have selected a few that might work - but I am not sure. We are open to your ideas so please do not feel the need to use all or any of these.

```html
<!DOCTYPE html>
<html lang="en">
<head>
<meta charset="utf-8">
<title>Morvane Equity LLC — Business Card</title>
<link rel="stylesheet" href="https://fonts.googleapis.com/css2?family=Libre+Baskerville&family=Open+Sans:wght@400;600;700&display=swap">
<style>
  :root {
    --bg: #2b2d31;
    --blue: #0d56b0;
    --blue-text: #1f57b4;
    --blue-faint: rgba(255,255,255,0.07);
    --grey: #a3a5a8;
    --grey-dark: #8e9093;
    --ink: #444649;
    --white: #ffffff;
  }
  * { margin: 0; padding: 0; box-sizing: border-box; }
  html, body { width: 1200px; height: 900px; overflow: hidden; background: var(--bg); }
  .sheet {
    width: 1200px; height: 900px;
    display: flex; align-items: center; justify-content: center; gap: 40px;
  }
  .card {
    position: relative; width: 540px; height: 310px; overflow: hidden;
    box-shadow: 0 14px 30px rgba(0,0,0,0.45);
  }
  .card-shape { position: absolute; inset: 0; }

  /* Front */
  .front-logo {
    position: absolute; left: 52px; top: 78px;
    font-family: "Libre Baskerville", "Times New Roman", serif;
    font-size: 25px; line-height: 1.25; letter-spacing: 0.5px;
    color: var(--blue-text); text-transform: uppercase;
  }
  .front-logo span { display: block; }
  .front-logo .line-1 { padding-left: 42px; }
  .divider {
    position: absolute; left: 236px; top: 104px; width: 1.5px; height: 108px;
    background: var(--grey-dark);
  }
  .contact {
    position: absolute; left: 252px; top: 106px;
    font-family: "Open Sans", Arial, sans-serif; color: var(--ink);
  }
  .person-name { font-size: 22px; font-weight: 700; letter-spacing: 0.5px; line-height: 1.1; }
  .person-title { font-size: 12px; font-weight: 700; color: var(--blue-text); letter-spacing: 0.6px; margin-top: 2px; }
  .contact-row { display: flex; align-items: flex-start; gap: 8px; margin-top: 8px; font-size: 12px; font-weight: 600; }
  .contact-row svg { flex: none; }
  .address { font-variant: small-caps; line-height: 1.3; }

  /* Back */
  .back-watermark {
    position: absolute; left: 26px; top: 62px;
    font-family: "Libre Baskerville", "Times New Roman", serif;
    font-size: 66px; line-height: 1.05; color: var(--blue-faint); text-transform: uppercase;
    white-space: nowrap;
  }
  .back-watermark .line-1 { display: block; padding-left: 70px; }
  .back-name {
    position: absolute; left: 0; right: 0; top: 112px; text-align: center;
    font-family: "Libre Baskerville", "Times New Roman", serif;
    font-size: 19px; letter-spacing: 0.5px; color: var(--white); text-transform: uppercase;
  }
</style>
</head>
<body>
<main class="sheet">

  <section class="card card-front">
    <svg class="card-shape" width="540" height="310" viewBox="0 0 540 310">
      <rect width="540" height="310" fill="var(--white)"/>
      <rect width="540" height="8" fill="var(--blue)"/>
      <rect y="8" width="540" height="3" fill="var(--grey)"/>
      <path d="M0 296 H228 Q238 262 262 262 H540 V310 H0 Z" fill="var(--blue)"/>
      <path d="M0 294 H226 Q236 259 262 259 H540" fill="none" stroke="var(--grey)" stroke-width="3"/>
    </svg>
    <div class="front-logo"><span class="line-1">Morvane</span><span>Equity LLC</span></div>
    <div class="divider"></div>
    <div class="contact">
      <div class="person-name">PETER DALBY</div>
      <div class="person-title">PORTFOLIO MANAGER</div>
      <div class="contact-row">
        <svg width="16" height="16" viewBox="0 0 16 16" aria-hidden="true">
          <circle cx="8" cy="8" r="8" fill="var(--blue-text)"/>
          <path d="M5.3 4.2l1.4-.4.8 1.8-.9.7c.4.9 1.1 1.7 2 2.1l.7-.9 1.8.8-.4 1.4c-2.9.2-5.6-2.6-5.4-5.5z" fill="var(--white)"/>
        </svg>
        <span>(412) 555-0187</span>
      </div>
      <div class="contact-row">
        <svg width="16" height="16" viewBox="0 0 16 16" aria-hidden="true">
          <circle cx="8" cy="8" r="8" fill="var(--blue-text)"/>
          <path d="M8 3.5a3 3 0 0 0-3 3c0 2.2 3 5.8 3 5.8s3-3.6 3-5.8a3 3 0 0 0-3-3z" fill="var(--white)"/>
          <circle cx="8" cy="6.5" r="1.1" fill="var(--blue-text)"/>
        </svg>
        <span class="address">2650 Birchmont Lane, Suite 300,<br>Atlanta GA 30327</span>
      </div>
    </div>
  </section>

  <section class="card card-back">
    <svg class="card-shape" width="540" height="310" viewBox="0 0 540 310">
      <rect width="540" height="310" fill="var(--blue)"/>
      <rect width="540" height="12" fill="var(--grey)"/>
      <path d="M0 296 H228 Q238 262 262 262 H540 V310 H0 Z" fill="var(--grey)"/>
    </svg>
    <div class="back-watermark" aria-hidden="true"><span class="line-1">Morvane</span>Equity LLC</div>
    <div class="back-name">Morvane Equity LLC</div>
  </section>

</main>
</body>
</html>
```